Flaschenetikett für veganen Sirup mit 100% Biozutaten
Zielgruppe
Wir stellen einen 100% biologisch, veganen Chai-Sirup in Handarbeit her;
Zielgruppe: jugendliche, Veganer, Kaffeetrinker, Teetrinker, Hipster, im Prinzip jeder der auf Würzige Getränke steht
Aufgabenstellung
nicht zu detailliert, modern, leichte ayurvedische Note,
Schraubverschluss der Flasche ist schwarz.
Etikettengröße: max. 188mm Breite, max. 105mm Höhe.
Maße können zur Gestaltung komplett genutzt werden - kein muss - hier ist der Designer gefragt ;-)
Aufdruck: Logo, Chai Sirup, Barcode, Nährwerttabelle (Werte sind noch in Berechnung, kommen im Laufe der Woche), Zutatenliste (Wasser, Rohrohrzucker*, Zimt*, Ingwer*, Vanillezucker*, Pfeffer schwarz*, Koriandersamen*, Kardamom*, Sternanis*, Piment*, Nelken*) mit * gekennzeichnete Zutaten stammen aus kontrolliert biologischem Anbau.
Unsere Domain lerno-tabu.com sowie 'Lerno Tabu GbR, Tannhecke 47, 91126 Schwabach' muss ebenfalls auf das Etikett.
Benötigt wird auch ein weißes Feld für die Chargennummer und das MHD, welche von uns per Stempel angebracht werden.
Im Moment warten wir noch auf die Freigabe des Bio Siegels, das im Nachgang noch auf der Vorderseite des Etiketts von uns eingefügt wird. Hierfür bei der Gestaltung Platz berücksichtigen.
Auf der Rückseite wird sich das Etikett nicht ganz berühren, so dass man den Füllstand der Flasche noch erkennen kann.

```html
<!DOCTYPE html>
<html lang="de">
<head>
<meta charset="utf-8">
<title>Chai Sirup – Flaschenetikett</title>
<link rel="stylesheet" href="https://fonts.googleapis.com/css2?family=Kaushan+Script&family=Alegreya:ital,wght@0,500;1,400&display=swap">
<style>
  :root {
    --backdrop: #e4e3e8;
    --label-black: #050505;
    --leaf-green: #2f9a45;
    --elephant-green: #0f3a1c;
    --gold: #c9a044;
    --white: #ffffff;
  }
  html, body {
    margin: 0;
    padding: 0;
    width: 1200px;
    height: 849px;
    overflow: hidden;
    background: var(--backdrop);
  }
  .canvas {
    position: relative;
    width: 1200px;
    height: 849px;
  }
  .label-art {
    position: absolute;
    inset: 0;
  }
  .brand-mark {
    position: absolute;
    left: 542px;
    top: 217px;
    width: 84px;
    height: 84px;
    display: flex;
    align-items: center;
    justify-content: center;
  }
  .brand-name {
    font-family: "Alegreya", Georgia, serif;
    font-weight: 500;
    font-size: 11px;
    letter-spacing: 0.5px;
    color: var(--gold);
    text-transform: uppercase;
    white-space: nowrap;
  }
  .product-title {
    position: absolute;
    left: 0;
    width: 1200px;
    top: 362px;
    margin: 0;
    text-align: center;
    font-family: "Kaushan Script", cursive;
    font-weight: 400;
    font-size: 86px;
    line-height: 1;
    color: var(--white);
  }
  .product-claim {
    position: absolute;
    left: 0;
    width: 1200px;
    top: 464px;
    margin: 0;
    text-align: center;
    font-family: "Alegreya", Georgia, serif;
    font-style: italic;
    font-weight: 400;
    font-size: 33px;
    line-height: 1;
    color: var(--white);
  }
</style>
</head>
<body>
<main class="canvas">
  <svg class="label-art" width="1200" height="849" viewBox="0 0 1200 849">
    <defs>
      <radialGradient id="elephant-tone" cx="50%" cy="50%" r="50%">
        <stop offset="0%" stop-color="#0f3a1c" stop-opacity="0.9"/>
        <stop offset="100%" stop-color="#0f3a1c" stop-opacity="0"/>
      </radialGradient>
    </defs>
    <ellipse class="label-shape" cx="600" cy="439" rx="277" ry="229" fill="var(--label-black)"/>
    <ellipse class="elephant-illustration" role="img" aria-label="Dezentes, grün ornamentiertes Elefantenmotiv im Mandala-Stil"
             cx="602" cy="452" rx="195" ry="145" fill="url(#elephant-tone)"/>
    <g class="leaf-wreath" role="img" aria-label="Grüner, gezeichneter Blätterkranz um den Produktnamen"
       fill="none" stroke="var(--leaf-green)" stroke-width="22" stroke-linecap="round" opacity="0.85">
      <path d="M505 252 Q368 330 372 455 Q380 590 560 622"/>
      <path d="M695 252 Q832 330 828 455 Q820 590 640 622"/>
    </g>
    <circle class="brand-ring" cx="584" cy="259" r="42" fill="var(--label-black)" stroke="var(--gold)" stroke-width="1.5"/>
  </svg>

  <div class="brand-mark">
    <span class="brand-name">Lerno Tabu</span>
  </div>

  <h1 class="product-title">Chai Sirup</h1>
  <p class="product-claim">100% Organic, Vegan</p>
</main>
</body>
</html>
```